Natural/Holistic/Spiritual Product Line ( Body Scrubs, Essential Oils, Lotions, Herbs, Candles, e...

I need Product labels that I can use interchangeably for my company "Marisol Glade" I make natural products such as body scrubs, bath salts, candles, essential oil blends, salves, body butters, etc. I want simple, but elegant labels. I want designs that use green, white and earth tones. My products are all natural, homegrown, handcrafted. Materials are all able to be recycled or are biodegradable.

Target Market(s)

Holistic, Natural, Organic, Herbalism - Body, Mind & Spirit encompassing products

Industry/Entity Type

Skin Care Product

Font styles to use
Sans Serif
Decorative
Script

Colors

Designer to choose colors to be used in the design.

Requirements
Must have
• My logo and simple, elegant designs. I have other logo files I can provide you as well, just ask.
Nice to have
• Surprise me!
Should not have
• Nothing flashy.

```html
<!DOCTYPE html>
<html lang="en">
<head>
<meta charset="utf-8">
<title>Marisol Glade – Essential Oil Roll-On Label</title>
<link rel="stylesheet" href="https://fonts.googleapis.com/css2?family=Cinzel:wght@400;500&family=Comfortaa:wght@300;400&family=Open+Sans:wght@400&display=swap">
<style>
  :root {
    --page-bg: #f3f3f1;
    --label-green: #1f7a46;
    --label-green-deep: #17633a;
    --ink-green: #1b5a35;
    --white: #ffffff;
    --soft-white: rgba(255, 255, 255, 0.78);
  }
  * { margin: 0; padding: 0; box-sizing: border-box; }
  html, body {
    width: 1200px;
    height: 1200px;
    overflow: hidden;
    background: var(--page-bg);
  }
  .canvas {
    position: relative;
    width: 1200px;
    height: 1200px;
  }
  .label {
    position: absolute;
    left: 371px;
    top: 62px;
    width: 458px;
    height: 1075px;
    background: linear-gradient(90deg, var(--label-green-deep) 0%, var(--label-green) 18%, var(--label-green) 82%, var(--label-green-deep) 100%);
    overflow: hidden;
  }
  .brand {
    position: absolute;
    top: 168px;
    left: 0;
    width: 100%;
    text-align: center;
    font-family: "Comfortaa", "Quicksand", sans-serif;
    font-weight: 300;
    font-size: 36px;
    letter-spacing: 0.5px;
    color: var(--white);
  }
  .brand-dot {
    position: absolute;
    top: 80px;
    left: 50%;
    width: 40px;
    height: 40px;
    margin-left: -20px;
    border-radius: 50%;
    border: 3px solid var(--white);
  }
  .title-band {
    position: absolute;
    left: 152px;
    top: 255px;
    width: 150px;
    height: 820px;
    background: var(--white);
  }
  .title-divider {
    position: absolute;
    left: 252px;
    top: 255px;
    width: 4px;
    height: 820px;
    background: var(--label-green);
  }
  .product-name,
  .product-type,
  .description {
    position: absolute;
    writing-mode: vertical-rl;
    transform: rotate(180deg);
    white-space: nowrap;
  }
  .product-name {
    left: 160px;
    top: 280px;
    height: 770px;
    font-family: "Cinzel", "Trajan Pro", serif;
    font-weight: 500;
    font-size: 76px;
    line-height: 88px;
    color: var(--ink-green);
    text-align: center;
    letter-spacing: 1px;
  }
  .product-type {
    left: 262px;
    top: 280px;
    height: 260px;
    font-family: "Cinzel", serif;
    font-size: 24px;
    line-height: 32px;
    letter-spacing: 1px;
    color: var(--ink-green);
    text-align: right;
  }
  .accent-line {
    position: absolute;
    left: 320px;
    top: 255px;
    width: 4px;
    height: 770px;
    background: var(--white);
  }
  .volume {
    position: absolute;
    left: 362px;
    top: 998px;
    font-family: "Open Sans", sans-serif;
    font-size: 21px;
    color: var(--soft-white);
  }
  .description {
    left: 8px;
    top: 230px;
    height: 760px;
    font-family: "Open Sans", sans-serif;
    font-size: 15px;
    line-height: 22px;
    color: var(--soft-white);
    text-align: right;
    white-space: normal;
  }
</style>
</head>
<body>
  <main class="canvas">
    <section class="label" aria-label="Essential oil roll-on label">
      <span class="brand-dot" aria-hidden="true"></span>
      <div class="brand">marisol glade</div>

      <p class="description">Soothes body and mind with a calming blend of lavender and ginger that leaves skin<br>brighter and elastic, coupled with the natural aroma of herbs</p>

      <div class="title-band"></div>
      <div class="title-divider"></div>
      <h1 class="product-name">ESSENTIAL OIL</h1>
      <p class="product-type">ROLL - ON</p>

      <div class="accent-line"></div>
      <p class="volume">10 ml</p>
    </section>
  </main>
</body>
</html>
```